I need a business card design for a new dance business. I offer classical Indian dance tuition and also professional performances. I want to offer the community a variety of Indian dance experiences which include: group class and private tuition, school and preschool educational courses and workshops. dance theatre performances, community function workshops and performances, Kids Bollywood parties, wedding & conference performances, mouth percussion classes, Indian mythology/ dance costume and make up workshops.
The final design should communicate a feeling and impression of the vibrance and energy of Indian dance.
Updates
Hi Everyone,
Project Deadline Extended
Reason: I would like to refine a few changes to the details of this lovely design and we have run out of time!
Project Deadline Extended
Reason: Still waiting to hear back form designer re two possible changes to the card design. Tomorrow is the deadline and I have sent several messages but with no response. I need to see this through before selecting this lovely design.
Thank you.
Tara
Industry/Entity Type
Preschool
Requirements
Must have
- The front of the business card should have the photo of me (my face and torso), surrounded entirely by a border of bright magenta (to match the magenta of my lipstick - it is the same as the magenta on my skirt in the second photo). Within the top border I want (perhaps yellow-gold) writing to say "Tara Holloway - Artistic Director" and within the bottom border it should read "Silver Creek Kathak Studio." If you turn the card on its side the left border should have my telephone number: 0417 826 394 and the right-hand border should read: silvercreekkathakstudio@fernmail.example
The reverse of the card should be the orange of the dance costume
and I'd like the picture of my feet and legs to be on the right side of the back of the card as a side border. Centre-aligned on the orange background it should read (perhaps in dark magenta):
Indian dance classes + private tuition
School + preschool educational courses and workshops
Dance theatre performances
Community function workshops and performances
Children's Bollywood parties
Wedding + conference performances
Mouth percussion classes
Indian mythology and dance demonstration workshops
Dance costume and make-up workshops
Nice to have
- A lovely artistic but easy-to-read font would be nice.

```html
<!DOCTYPE html>
<html lang="en">
<head>
<meta charset="utf-8">
<title>Silver Creek Kathak Studio – Business Card</title>
<link rel="stylesheet" href="https://fonts.googleapis.com/css2?family=Great+Vibes&family=Crimson+Text:ital,wght@0,400;0,600;1,400&display=swap">
<style>
  :root {
    --backdrop: #2b0707;
    --gold-light: #ffd21a;
    --gold: #f8bd00;
    --orange: #f39a00;
    --plum: #8a1d6e;
    --wine: #9c1c3a;
    --brick: #a4361c;
    --maroon: #6e0f2a;
    --magenta: #b0216a;
    --cream: #fff3b0;
    --white: #ffffff;
  }
  * { margin: 0; padding: 0; box-sizing: border-box; }
  html, body {
    width: 1200px; height: 900px; overflow: hidden;
    background: var(--backdrop);
  }
  .stage { position: relative; width: 1200px; height: 900px; }

  .card {
    position: absolute; top: 110px;
    width: 440px; height: 670px;
    overflow: hidden;
    box-shadow: 0 6px 18px rgba(0,0,0,.55);
  }
  .card--front {
    left: 114px;
    background: linear-gradient(180deg, var(--gold-light) 0%, var(--gold) 45%, var(--orange) 100%);
  }
  .card--back {
    left: 654px;
    background: radial-gradient(ellipse at 40% 50%, var(--gold-light) 0%, var(--gold) 50%, var(--orange) 100%);
  }

  /* front */
  .front-photo {
    position: absolute; left: 186px; top: 0; width: 254px; height: 612px;
    background:
      radial-gradient(ellipse at 40% 35%, rgba(245,180,60,.85) 0%, rgba(245,180,60,0) 45%),
      linear-gradient(180deg, var(--maroon) 0%, var(--magenta) 40%, #c86a3a 75%, rgba(248,170,0,0) 100%);
    opacity: .9;
  }
  .studio-name {
    position: absolute; left: 22px; top: 64px;
    font-family: "Great Vibes", cursive;
    font-size: 46px; line-height: 56px;
    color: var(--plum);
  }
  .studio-name span { display: block; }
  .studio-name span + span { padding-left: 46px; }

  .contact {
    position: absolute; left: 22px; top: 466px;
    font-family: "Crimson Text", serif;
    color: var(--brick);
  }
  .contact__name { font-size: 27px; font-weight: 400; letter-spacing: .3px; }
  .contact__role { margin-top: 16px; font-size: 18px; line-height: 23px; }
  .contact__phone { margin-top: 16px; font-size: 18px; }

  .email-bar {
    position: absolute; left: 0; bottom: 0; width: 100%; height: 48px;
    background: var(--gold);
    border-top: 2px dotted var(--cream);
    display: flex; align-items: center; padding-left: 20px;
    font-family: "Crimson Text", serif; font-style: italic;
    font-size: 17px; color: var(--plum);
  }

  /* back */
  .services {
    position: absolute; left: -221px; top: 265px;
    width: 630px; height: 160px;
    transform: rotate(-90deg);
    display: flex; gap: 14px;
    font-family: "Crimson Text", serif;
    font-size: 17.5px; line-height: 19px;
    color: var(--wine);
  }
  .services__col { flex: 1; list-style: none; }
  .services__col li { position: relative; padding-left: 18px; }
  .services__col li::before {
    content: ""; position: absolute; left: 2px; top: 5px;
    width: 9px; height: 9px; border-radius: 50%;
    background: #d0101e;
  }
  .back-photo {
    position: absolute; left: 196px; top: 14px; width: 232px; height: 646px;
    border-radius: 90px 90px 40px 40px;
    background:
      radial-gradient(ellipse at 50% 12%, #e7b48c 0%, rgba(231,180,140,0) 18%),
      linear-gradient(180deg, #d89a3a 0%, var(--maroon) 35%, #8b1a2e 65%, #c99a3a 85%, var(--maroon) 100%);
    box-shadow: 0 0 0 6px rgba(255,255,255,.85);
  }
</style>
</head>
<body>
<main class="stage">
  <section class="card card--front">
    <div class="front-photo" role="img" aria-label="Photo of a classical Indian dancer in a magenta and gold costume, mid-pose with hands and a raised leg"></div>
    <h1 class="studio-name"><span>Silver Creek</span><span>Kathak Studio</span></h1>
    <div class="contact">
      <p class="contact__name">Tara Holloway</p>
      <p class="contact__role">Graduate of Kuchipudi<br>classical Indian dance</p>
      <p class="contact__phone">T. 0417 826 394</p>
    </div>
    <p class="email-bar">E. silvercreekkathakstudio@fernmail.example</p>
  </section>

  <section class="card card--back">
    <div class="services">
      <ul class="services__col">
        <li>Indian dance classes +<br>private tuition</li>
        <li>School + preschool educational<br>courses and workshops</li>
        <li>Dance theatre performances</li>
        <li>Community function workshops<br>and performances</li>
      </ul>
      <ul class="services__col">
        <li>Children’s parties</li>
        <li>Wedding + conference<br>performances</li>
        <li>Mouth percussion classes</li>
        <li>Indian mythology and<br>dance demonstration<br>workshops</li>
      </ul>
    </div>
    <div class="back-photo" role="img" aria-label="Full-length photo of a classical Indian dancer in a maroon and gold pleated costume with jewellery"></div>
  </section>
</main>
</body>
</html>
```